Corwen Physical Therapy Website

I would need a clean modern website built to showcase my Physical therapy brand and services. I would need a simple but descriptive website that can ultimately connect my patients to my electronic medical portal so they may book an appointment..

```html
<!DOCTYPE html>
<html lang="en">
<head>
<meta charset="utf-8">
<title>Corwen Physical Therapy</title>
<link href="https://fonts.googleapis.com/css2?family=Poppins:ital,wght@0,400;0,500;0,600;0,700;1,400&display=swap" rel="stylesheet">
<style>
:root{
  --teal:#11877d;
  --teal-dark:#0c6f66;
  --blue:#4a5bb3;
  --navy:#1f2a3a;
  --ink:#222;
  --muted:#555;
  --footer:#1c1c1c;
  --grey-card:#d6d6d6;
  --gold:#f2a93b;
  --white:#fff;
}
*{box-sizing:border-box;margin:0;padding:0}
html,body{width:1200px;height:4356px;overflow:hidden}
body{font-family:'Poppins',sans-serif;color:var(--ink);background:var(--white)}
.page{position:relative;width:1200px;height:4356px;overflow:hidden}
.abs{position:absolute}
.btn{position:absolute;display:flex;align-items:center;justify-content:center;border-radius:30px;font-weight:600;font-size:13px;letter-spacing:.5px;text-transform:uppercase}
.btn-teal{background:var(--teal);color:var(--white)}
.btn-white{background:var(--white);color:var(--ink)}
.section-title{position:absolute;left:0;width:1200px;text-align:center;font-size:31px;letter-spacing:1px;text-transform:uppercase}
.section-title b{font-weight:700}
.section-title span{font-weight:400}
.section-title::before{content:"";display:inline-block;width:3px;height:30px;background:currentColor;margin-right:10px;vertical-align:-4px}
.title-light{color:var(--white)}
.title-light::before{background:var(--white)}
.title-dark::before{background:var(--blue)}

/* hero */
.hero-photo{left:0;top:0;width:1200px;height:700px;background:linear-gradient(120deg,#f2eee9 0%,#e4d9d2 35%,#c9c3c6 60%,#b7b5bd 100%)}
.hero-veil{left:0;top:0;width:1200px;height:700px;background:linear-gradient(180deg,rgba(255,255,255,.55),rgba(255,255,255,.15) 60%,rgba(255,255,255,0))}
.brand{display:flex;align-items:center;gap:10px;color:var(--teal);font-weight:700}
.brand-dot{width:18px;height:18px;border-radius:50%;background:var(--teal)}
.site-brand{left:108px;top:48px;font-size:30px}
.nav{left:367px;top:52px;display:flex;font-size:15px;color:#333}
.nav a{position:absolute;white-space:nowrap;text-decoration:none;color:#333;text-transform:uppercase}
.nav .active{color:var(--teal)}
.contact-btn{left:961px;top:43px;width:128px;height:42px;font-size:12px}
.hero-arrow{width:56px;height:56px;border-radius:50%;border:2px solid #555;display:flex;align-items:center;justify-content:center;color:#333;font-size:18px}
.hero-title{left:0;top:268px;width:1200px;text-align:center;font-size:43px;font-weight:600;color:#222}
.hero-sub{left:290px;top:334px;width:620px;text-align:center;font-size:16px;line-height:27px;color:#222}
.hero-cta{left:519px;top:401px;width:162px;height:41px}

/* about */
.about-ring{left:118px;top:784px;width:482px;height:482px;border-radius:50%;border:8px solid var(--navy);padding:10px;background:var(--white)}
.about-photo{width:100%;height:100%;border-radius:50%;background:linear-gradient(150deg,#e9e5df,#c9c3bd 55%,#8f8a86)}
.about-text{left:638px;top:818px;width:440px}
.about-title{font-size:31px;letter-spacing:1px;text-transform:uppercase;display:flex;align-items:center;gap:10px}
.about-title::before{content:"";width:3px;height:30px;background:var(--blue)}
.about-lead{margin-top:16px;font-size:16.5px;font-weight:600;line-height:26px;color:#222}
.about-body{margin-top:14px;font-size:13.2px;line-height:22px;color:var(--muted)}
.about-cta{left:638px;top:1185px;width:162px;height:43px}

/* services */
.services{left:0;top:1352px;width:1200px;height:666px;background:var(--teal)}
.service-card{position:absolute;top:142px;width:301px;height:372px}
.service-photo{width:301px;height:299px}
.service-label{position:absolute;left:8px;top:290px;width:285px;height:64px;background:var(--white);display:flex;align-items:center;justify-content:center;font-size:17px;color:#222;box-shadow:0 3px 8px rgba(0,0,0,.15)}
.services-cta{left:519px;top:537px;width:162px;height:43px}

/* benefits */
.benefits{left:0;top:2018px;width:1200px;height:582px}
.benefit{position:absolute;width:360px}
.benefit h4{font-size:17px;font-weight:500;color:#222}
.benefit p{font-size:13.2px;line-height:22px;color:var(--muted);margin-top:2px}
.benefit.left{text-align:right}
.benefit-icon{position:absolute;width:60px;height:60px;border-radius:50%;background:var(--teal);border:4px solid #e4f1ef;display:flex;align-items:center;justify-content:center}
.hub{left:467px;top:191px;width:270px;height:270px;border-radius:50%;background:var(--white);box-shadow:0 4px 18px rgba(0,0,0,.14);display:flex;align-items:center;justify-content:center}
.hub .brand{font-size:36px}

/* blog */
.blog{left:0;top:2600px;width:1200px;height:699px;background:var(--blue)}
.blog-feature{left:113px;top:148px;width:519px;height:390px;background:linear-gradient(160deg,#e7eef4,#b9c8d8 50%,#41505f)}
.blog-feature-shade{left:0;top:0;width:519px;height:390px;background:linear-gradient(180deg,rgba(0,0,0,0) 45%,rgba(0,0,0,.8))}
.date-badge{position:absolute;background:#111;color:var(--white);text-align:center;font-weight:500}
.feature-date{left:20px;top:22px;width:72px;height:68px;font-size:26px;padding-top:6px;line-height:28px}
.feature-date small{display:block;font-size:15px;letter-spacing:5px}
.feature-date sup{font-size:13px}
.feature-title{left:20px;top:262px;width:480px;font-size:17px;font-weight:600;line-height:26px;color:var(--white)}
.feature-sub{left:20px;top:328px;width:480px;font-size:13px;line-height:22px;color:var(--white)}
.blog-item{position:absolute;left:655px;width:432px;height:115px;background:var(--grey-card)}
.blog-thumb{position:absolute;left:0;top:0;width:165px;height:115px;background:linear-gradient(150deg,#dce5ec,#8da1b3 60%,#55606c)}
.small-date{left:6px;top:6px;width:38px;height:40px;font-size:15px;line-height:18px;padding-top:3px}
.small-date small{display:block;font-size:9px;letter-spacing:3px}
.small-date sup{font-size:8px}
.blog-item p{position:absolute;left:182px;top:30px;width:230px;font-size:12.5px;font-weight:600;line-height:21px;color:#222}
.blog-cta{left:519px;top:572px;width:162px;height:41px}

/* testimonials */
.testi-title{top:3372px}
.testi-card{position:absolute;top:3444px;height:260px;background:var(--white);box-shadow:0 2px 14px rgba(0,0,0,.12)}
.testi-photo{position:absolute;background:linear-gradient(160deg,#8a8a8a,#4b4b4b 60%,#2f2f2f)}
.testi-quote{font-size:13px;font-style:italic;line-height:22px;color:#666}
.stars{color:var(--gold);font-size:18px;letter-spacing:2px}
.testi-name{font-size:15px;font-weight:500;color:var(--teal);text-transform:uppercase}
.testi-role{font-size:12px;color:#888}
.testi-arrow{width:40px;height:40px;border-radius:50%;border:2px solid var(--teal);display:flex;align-items:center;justify-content:center;color:var(--teal);font-size:15px}

/* footer */
.footer{left:0;top:3880px;width:1200px;height:476px}
.footer-brand{left:190px;top:4078px;font-size:34px}
.social{position:absolute;top:4204px;width:60px;height:60px;border-radius:50%;border:2px solid #cfcfcf}
.footer-col{position:absolute;top:4040px;color:var(--white)}
.footer-col h5{font-size:21px;font-weight:500}
.footer-col h5::after{content:"";display:block;width:44px;height:2px;background:var(--teal);margin-top:12px}
.footer-col ul{list-style:none;margin-top:20px}
.footer-col li{font-size:13.5px;line-height:28px}
.footer-rule{left:150px;top:4280px;width:950px;height:1px;background:#444}
.copyright{left:0;top:4313px;width:1200px;text-align:center;color:var(--white);font-size:13.5px}
.copyright em{font-style:normal;color:var(--teal)}
</style>
</head>
<body>
<div class="page">

  <!-- hero -->
  <div class="abs hero-photo" role="img" aria-label="Photo of a therapist stretching a patient's leg on a treatment table"></div>
  <div class="abs hero-veil"></div>
  <svg class="abs" style="left:0;top:600px" width="1200" height="100" viewBox="0 0 1200 100">
    <path d="M0 40 C300 100 620 115 860 50 C980 20 1100 10 1200 20 L1200 100 L0 100 Z" fill="#fff"/>
    <path d="M0 40 C300 100 620 115 860 50 C980 20 1100 10 1200 20" fill="none" stroke="var(--blue)" stroke-width="5"/>
  </svg>
  <div class="abs brand site-brand"><span class="brand-dot"></span>CORWEN</div>
  <nav class="abs nav">
    <a class="active" style="left:0">Home</a>
    <a style="left:90px">About Us</a>
    <a style="left:216px">Services</a>
    <a style="left:340px">Blog</a>
    <a style="left:427px">Testimonials</a>
  </nav>
  <div class="btn btn-teal contact-btn">Contact Us</div>
  <div class="abs hero-arrow" style="left:25px;top:318px">&#8249;</div>
  <div class="abs hero-arrow" style="left:1118px;top:318px">&#8250;</div>
  <h1 class="abs hero-title">Corwen Physical Therapy</h1>
  <p class="abs hero-sub">Perspiciatis unde omnis iste natus error sit voluptatem accusantium doloremque laudantium totam rem aperiam.</p>
  <div class="btn btn-teal hero-cta">Get Started</div>

  <!-- about -->
  <div class="abs about-ring"><div class="about-photo" role="img" aria-label="Photo of a therapist raising a patient's leg during treatment"></div></div>
  <div class="abs about-text">
    <h2 class="about-title"><span><b>About</b> Us</span></h2>
    <p class="about-lead">Perspiciatis unde omnis iste natus error sit voluptatem accusantium doloremque laudantium, totam rem aperiam, eaque ipsa quae ab illo inventore veritatis</p>
    <p class="about-body">Usjeuisb unde omnis iste natus error sit voluptatem accusantium doloremque laudantium, totam rem aperiam, eaque ipsa quae ab illo inventore veritatis et quasi architecto beatae vitae dicta sunt explicabo. Nemo enim ipsam voluptatem quia voluptas sit aspernatur aut odit aut fugit, sed quia consequuntur magni dolores eos qui ratione voluptatem sequi nesciunt. Neque porro quisquam est, qui dolorem ipsum quia dolor sit amet</p>
  </div>
  <div class="btn btn-teal about-cta">Learn More</div>

  <!-- services -->
  <section class="abs services">
    <h2 class="section-title title-light" style="top:82px"><b>Our</b> <span>Services</span></h2>
    <div class="service-card" style="left:111px">
      <div class="service-photo" role="img" aria-label="Photo of a therapist treating a patient's back" style="background:linear-gradient(160deg,#e8e3dd,#b7a99c 55%,#3c6fa3)"></div>
      <div class="service-label">Perspiciatis unde omnis</div>
    </div>
    <div class="service-card" style="left:450px">
      <div class="service-photo" role="img" aria-label="Photo of two men exercising with small dumbbells" style="background:linear-gradient(160deg,#dfe3e6,#9aa0a6 50%,#e2742f 80%,#5d6166)"></div>
      <div class="service-label">Perspiciatis unde omnis</div>
    </div>
    <div class="service-card" style="left:788px">
      <div class="service-photo" role="img" aria-label="Photo of a therapist stretching a patient on a mat" style="background:linear-gradient(160deg,#eceae6,#b9c4c2 50%,#2e9a86 75%,#8a8088)"></div>
      <div class="service-label">Perspiciatis unde omnis</div>
    </div>
    <div class="btn btn-white services-cta">View More</div>
  </section>

  <!-- benefits -->
  <section class="abs benefits">
    <h2 class="section-title title-dark" style="top:79px;color:#222"><b>Benefits</b></h2>
    <svg class="abs" style="left:420px;top:144px" width="364" height="364" viewBox="0 0 364 364">
      <circle cx="182" cy="182" r="177" fill="none" stroke="#999" stroke-width="1.5" stroke-dasharray="6 5"/>
    </svg>
    <div class="abs hub"><div class="brand"><span class="brand-dot"></span>CORWEN</div></div>

    <div class="benefit-icon" style="left:435px;top:177px"><svg width="26" height="26" viewBox="0 0 26 26" fill="none" stroke="#fff" stroke-width="2"><circle cx="13" cy="7" r="4"/><path d="M5 23 C5 15 21 15 21 23"/></svg></div>
    <div class="benefit-icon" style="left:391px;top:296px"><svg width="26" height="26" viewBox="0 0 26 26" fill="none" stroke="#fff" stroke-width="2"><circle cx="13" cy="6" r="3"/><path d="M13 10 L13 17 L8 24 M13 17 L18 24 M7 13 L19 13"/></svg></div>
    <div class="benefit-icon" style="left:435px;top:418px"><svg width="26" height="26" viewBox="0 0 26 26" fill="none" stroke="#fff" stroke-width="2"><circle cx="13" cy="13" r="8"/><path d="M9 13 L12 16 L17 10"/></svg></div>
    <div class="benefit-icon" style="left:704px;top:177px"><svg width="26" height="26" viewBox="0 0 26 26" fill="none" stroke="#fff" stroke-width="2"><path d="M3 13 L23 13 M6 9 L6 17 M20 9 L20 17"/></svg></div>
    <div class="benefit-icon" style="left:751px;top:296px"><svg width="26" height="26" viewBox="0 0 26 26" fill="none" stroke="#fff" stroke-width="2"><circle cx="11" cy="6" r="3"/><path d="M11 10 L11 18 L17 18 L19 24 M6 14 L11 12"/></svg></div>
    <div class="benefit-icon" style="left:704px;top:418px"><svg width="26" height="26" viewBox="0 0 26 26" fill="none" stroke="#fff" stroke-width="2"><path d="M4 18 L13 6 L22 18 Z"/><path d="M13 11 L13 15"/></svg></div>

    <div class="benefit left" style="left:63px;top:196px"><h4>Perspiciatis unde omnis</h4><p>Usjeuisb unde omnis iste natus error sit volup tatem accusantium doloremque.</p></div>
    <div class="benefit left" style="left:11px;top:318px"><h4>Perspiciatis unde omnis</h4><p>Usjeuisb unde omnis iste natus error sit volup tatem accusantium doloremque.</p></div>
    <div class="benefit left" style="left:63px;top:440px"><h4>Perspiciatis unde omnis</h4><p>Usjeuisb unde omnis iste natus error sit volup tatem accusantium doloremque.</p></div>
    <div class="benefit" style="left:781px;top:196px"><h4>Perspiciatis unde omnis</h4><p>Usjeuisb unde omnis iste natus error sit volup tatem accusantium doloremque.</p></div>
    <div class="benefit" style="left:829px;top:318px"><h4>Perspiciatis unde omnis</h4><p>Usjeuisb unde omnis iste natus error sit volup tatem accusantium doloremque.</p></div>
    <div class="benefit" style="left:781px;top:440px"><h4>Perspiciatis unde omnis</h4><p>Usjeuisb unde omnis iste natus error sit volup tatem accusantium doloremque.</p></div>
  </section>

  <!-- blog -->
  <section class="abs blog">
    <h2 class="section-title title-light" style="top:79px"><b>Our</b> <span>Blog</span></h2>
    <div class="abs blog-feature" role="img" aria-label="Photo of a therapist adjusting a woman's shoulder">
      <div class="abs blog-feature-shade"></div>
      <div class="date-badge feature-date">15<sup>th</sup><small>MAY</small></div>
      <p class="abs feature-title">Kaistam rem aperia eaque ipsa quae ab illo inventore veritatis et quasi architecto beatae.</p>
      <p class="abs feature-sub">Perspiciatis unde omnis iste natus error sit voluptatem accusantium doloremque laudantium, totam rem aperia.</p>
    </div>
    <div class="blog-item" style="top:148px">
      <div class="blog-thumb" role="img" aria-label="Photo of a group exercise class"><div class="date-badge small-date">15<sup>th</sup><small>MAY</small></div></div>
      <p>Kaistam rem aperia eaque ipsa quae ab illo inventore veritatis et quasi architecto beatae.</p>
    </div>
    <div class="blog-item" style="top:286px">
      <div class="blog-thumb" role="img" aria-label="Photo of a therapist treating a patient's knee"><div class="date-badge small-date">15<sup>th</sup><small>MAY</small></div></div>
      <p>Kaistam rem aperia eaque ipsa quae ab illo inventore veritatis et quasi architecto beatae.</p>
    </div>
    <div class="blog-item" style="top:423px">
      <div class="blog-thumb" role="img" aria-label="Photo of a therapist guiding a standing exercise"><div class="date-badge small-date">15<sup>th</sup><small>MAY</small></div></div>
      <p>Kaistam rem aperia eaque ipsa quae ab illo inventore veritatis et quasi architecto beatae.</p>
    </div>
    <div class="btn btn-white blog-cta">View More</div>
  </section>

  <!-- testimonials -->
  <h2 class="section-title title-dark testi-title" style="color:#222"><b>Testimonials</b></h2>
  <div class="testi-card" style="left:-120px;width:340px">
    <p class="abs testi-quote" style="left:0;top:34px;width:320px;text-align:right">or sit voluptatem<br>um, totam rem aperiam,<br>veritatis et quasi architecto<br>Nemo enim ipsam voluptatem<br>dit aut fugit, sed quia<br>ui ratione.</p>
    <div class="abs stars" style="left:176px;top:200px">★★★★★</div>
  </div>
  <div class="testi-card" style="left:250px;width:711px">
    <div class="testi-photo" style="left:10px;top:15px;width:235px;height:239px" role="img" aria-label="Portrait photo of a smiling client"></div>
    <p class="abs testi-quote" style="left:268px;top:32px;width:420px">Usjeuisb unde omnis iste natus error sit voluptatem accusantium doloremque laudantium, totam rem aperiam, eaque ipsa quae ab illo inventore veritatis et quasi architecto beatae vitae dicta sunt explicabo. Nemo enim ipsam voluptatem quia voluptas sit aspernatur aut odit aut fugit, sed quia consequuntur magni dolores eos qui ratione.</p>
    <div class="abs testi-name" style="left:268px;top:188px">Dana R Whitlow</div>
    <div class="abs testi-role" style="left:268px;top:212px">CMO, Brightmere</div>
    <div class="abs stars" style="left:550px;top:200px">★★★★★</div>
  </div>
  <div class="testi-card" style="left:988px;width:260px">
    <div class="testi-photo" style="left:15px;top:15px;width:230px;height:239px;background:linear-gradient(160deg,#f1f1f1,#cfc6c0 55%,#8a6f5e)" role="img" aria-label="Portrait photo of a smiling client"></div>
  </div>
  <div class="abs testi-arrow" style="left:546px;top:3742px">&#8249;</div>
  <div class="abs testi-arrow" style="left:614px;top:3742px">&#8250;</div>

  <!-- footer -->
  <svg class="abs" style="left:0;top:3880px" width="1200" height="476" viewBox="0 0 1200 476">
    <path d="M0 48 C200 95 320 100 520 40 C700 -10 900 0 1200 70 L1200 476 L0 476 Z" fill="var(--footer)"/>
    <path d="M0 48 C200 95 320 100 520 40 C700 -10 900 0 1200 70" fill="none" stroke="var(--blue)" stroke-width="5"/>
  </svg>
  <div class="abs brand footer-brand"><span class="brand-dot"></span>CORWEN</div>
  <div class="social" style="left:151px" aria-label="Social profile"></div>
  <div class="social" style="left:241px" aria-label="Social profile"></div>
  <div class="social" style="left:331px" aria-label="Social profile"></div>
  <div class="footer-col" style="left:508px"><h5>Quick Links</h5><ul><li>Home</li><li>About Us</li><li>Services</li><li>Blog</li><li>Testimonials</li></ul></div>
  <div class="footer-col" style="left:745px"><h5>Links</h5><ul><li>Copyright</li><li>Legal</li><li>Privacy</li><li>Accessibility</li><li>Sitemap</li></ul></div>
  <div class="footer-col" style="left:939px"><h5>Category</h5><ul><li>Team</li><li>About Us</li><li>Careers</li><li>Our Values</li></ul></div>
  <div class="abs footer-rule"></div>
  <p class="abs copyright">Copyrights ©2021 <em>Corwen Physical Therapy</em>. All Rights Reserved</p>

</div>
</body>
</html>
```